Paperback Book Cover Design

I need a professional cover designed for my new book. You must use the design template enclosed. The title of the book is “Begin Building Wealth From Home Now!” The graphic used on the book cover should of course relate to making money online through various skills such as writing, graphic design, online marketing, photography, trading, Vendora etc. The graphic(s) used must demonstrate to the reader that the book gives various ways to make money online.

At the top of the book you must include the sub heading “Earn Cash From Home Series”. The main title of the book is “Begin Building Wealth From Home Now!”, which of course should be highly prominent on the front cover. The front cover must also include the author name, Gerald Finchley.

I have no preference to colours used so do be creative to create an eye catching cover design.

The spine of the book should include the main title and the author name. Feel free to use an image or images for the rear of the book and just add dummy text.

The winning designer must supply a layered psd file complete with all fonts and elements used.
Updates

Industry/Entity Type

Graphic Design

Requirements
Must have
• The winning designer must supply a layered psd file complete with all fonts and elements used.

```html
<!DOCTYPE html>
<html lang="en">
<head>
<meta charset="utf-8">
<title>Begin Building Wealth From Home Now! – Paperback Cover</title>
<link rel="stylesheet" href="https://fonts.googleapis.com/css2?family=Teko:wght@500;600&family=Ubuntu:wght@700&family=Cinzel:wght@400&family=Arimo&family=Tinos&display=swap">
<style>
  :root {
    --page-bg: #e8e6e3;
    --cover-grey: #cdcdcd;
    --glow-white: #ffffff;
    --ink-black: #141414;
    --accent-orange: #f26a12;
    --body-ink: #1e1e1e;
    --photo-pink: #e59ac0;
    --photo-grey: #d9d9d6;
  }
  * { box-sizing: border-box; margin: 0; padding: 0; }
  html, body { width: 1200px; height: 721px; overflow: hidden; }
  body {
    background: var(--page-bg);
    position: relative;
  }
  .cover-wrap {
    position: absolute;
    left: 130px; top: 20px;
    width: 940px; height: 680px;
    display: flex;
    background: var(--cover-grey);
    box-shadow: 0 6px 18px rgba(0,0,0,.25);
  }
  .title-block {
    font-family: "Teko", "Arial Narrow", sans-serif;
    font-weight: 600;
    text-transform: uppercase;
    text-align: center;
    line-height: .9;
    color: var(--ink-black);
  }
  .title-block .accent { color: var(--accent-orange); }

  /* Back cover */
  .back-cover {
    width: 429px; height: 100%;
    padding: 68px 34px 0 68px;
  }
  .back-cover .title-block { margin-bottom: 36px; }
  .back-cover .line-top { font-size: 58px; }
  .back-cover .line-mid { font-size: 58px; }
  .back-cover .line-end { font-size: 84px; }
  .back-blurb {
    font-family: "Arimo", Arial, sans-serif;
    font-size: 11.4px;
    line-height: 1.42;
    color: var(--body-ink);
    text-align: justify;
  }
  .author-bio {
    display: flex;
    gap: 20px;
    margin-top: 24px;
  }
  .author-photo-slot {
    flex: 0 0 80px; height: 116px;
    background: #ffffff;
  }
  .author-bio-text {
    font-family: "Tinos", "Times New Roman", serif;
    font-size: 11px;
    line-height: 1.3;
    color: var(--body-ink);
    text-align: justify;
  }
  .author-bio-text .bio-name { font-size: 16px; }

  /* Spine */
  .spine {
    width: 59px; height: 100%;
    display: flex;
    justify-content: center;
    padding-top: 38px;
  }
  .spine-text {
    writing-mode: vertical-rl;
    display: flex;
    align-items: center;
    gap: 26px;
    white-space: nowrap;
  }
  .spine-title {
    font-family: "Teko", "Arial Narrow", sans-serif;
    font-weight: 600;
    font-size: 27px;
    letter-spacing: .5px;
    color: var(--ink-black);
    text-transform: uppercase;
  }
  .spine-title .accent { color: var(--accent-orange); }
  .spine-author {
    font-family: "Cinzel", serif;
    font-size: 21px;
    letter-spacing: 1px;
    color: var(--ink-black);
  }

  /* Front cover */
  .front-cover {
    width: 452px; height: 100%;
    background: radial-gradient(ellipse 62% 34% at 50% 31%, var(--glow-white) 0%, rgba(255,255,255,.75) 45%, rgba(255,255,255,0) 100%), var(--cover-grey);
    display: flex;
    flex-direction: column;
    align-items: center;
    padding-top: 44px;
  }
  .series-heading {
    font-family: "Ubuntu", Arial, sans-serif;
    font-weight: 700;
    font-size: 21px;
    letter-spacing: 2.4px;
    text-transform: uppercase;
    color: var(--ink-black);
  }
  .cover-artwork {
    margin-top: 62px;
    width: 290px; height: 170px;
    border-radius: 50%;
    background: radial-gradient(circle at 32% 45%, var(--photo-pink) 0%, #f0c4da 28%, rgba(240,240,240,0) 52%),
                radial-gradient(circle at 70% 50%, var(--photo-grey) 0%, rgba(235,235,235,0) 40%);
  }
  .front-cover .title-block { margin-top: 58px; }
  .front-cover .line-top { font-size: 70px; }
  .front-cover .line-mid { font-size: 70px; }
  .front-cover .line-end { font-size: 104px; }
  .front-author {
    margin-top: 18px;
    font-family: "Cinzel", serif;
    font-size: 32px;
    letter-spacing: 1.5px;
    color: var(--ink-black);
  }
</style>
</head>
<body>
  <main class="cover-wrap">
    <section class="back-cover">
      <h2 class="title-block">
        <span class="line-top" style="display:block">Begin Building</span>
        <span class="line-mid accent" style="display:block">Wealth From Home</span>
        <span class="line-end" style="display:block">Now!</span>
      </h2>
      <p class="back-blurb">need a professional cover designed for my new book. You must use the design template enclosed. The title of the book is “Begin Building Wealth From Home Now!” The graphic used on the book cover should of course relate to making money online through various skills such as writing, graphic design, online marketing, photography, trading, Vendora etc. The graphic(s) used must demonstrate to the reader that the book gives various ways to make money online.</p>
      <div class="author-bio">
        <div class="author-photo-slot"></div>
        <p class="author-bio-text"><span class="bio-name">Gerald Finchley</span> The title of the book is “Begin Building Wealth From Home Now!” The graphic used on the book cover should of course relate to making money online through various skills such as writing, graphic design, online marketing, photography, trading, Vendora etc. The graphic(s) used must demonstrate to the reader that the book gives various ways to make m</p>
      </div>
    </section>

    <section class="spine">
      <div class="spine-text">
        <span class="spine-title">Begin Building <span class="accent">Wealth From Home</span> Now!</span>
        <span class="spine-author">Gerald Finchley</span>
      </div>
    </section>

    <section class="front-cover">
      <p class="series-heading">Earn Cash From Home Series</p>
      <div class="cover-artwork" role="img" aria-label="Photo of a pink piggy bank beside a white computer mouse"></div>
      <h1 class="title-block">
        <span class="line-top" style="display:block">Begin Building</span>
        <span class="line-mid accent" style="display:block">Wealth From Home</span>
        <span class="line-end" style="display:block">Now!</span>
      </h1>
      <p class="front-author">Gerald Finchley</p>
    </section>
  </main>
</body>
</html>
```